Business Card Design

We are a commercial real estate brokerage in San Francisco, leasing office buildings downtown.
I would like a clean, elegant look. Simple but powerful .

Industry/Entity Type

Business

Contact Information for Business Card

Colin Farrow
lic# 07281549
415.555.0172
colin@tarvo-commercial.example
tarvo-commercial.example

```html
<!DOCTYPE html>
<html lang="en">
<head>
<meta charset="utf-8">
<title>Tarvo Commercial — Business Card</title>
<link href="https://fonts.googleapis.com/css2?family=Carlito:wght@400;700&display=swap" rel="stylesheet">
<style>
  :root {
    --card-bg: #ffffff;
    --brand-blue: #6a93c4;
    --text-grey: #555759;
  }
  html, body {
    margin: 0;
    padding: 0;
    width: 1200px;
    height: 686px;
    overflow: hidden;
    background: var(--card-bg);
  }
  .card {
    position: relative;
    width: 1200px;
    height: 686px;
    background: var(--card-bg);
    font-family: "Carlito", "Calibri", sans-serif;
    overflow: hidden;
  }
  .accent-bands {
    position: absolute;
    inset: 0;
    width: 1200px;
    height: 686px;
  }
  .accent-bands polygon { fill: var(--brand-blue); }
  .brand {
    position: absolute;
    left: 80px;
    top: 118px;
    display: flex;
    align-items: center;
    gap: 44px;
  }
  .brand-square {
    width: 170px;
    height: 170px;
    background: var(--brand-blue);
  }
  .brand-name {
    color: var(--brand-blue);
    font-weight: 700;
    line-height: 0.9;
    text-transform: uppercase;
  }
  .brand-name .primary {
    display: block;
    font-size: 134px;
    letter-spacing: 4px;
  }
  .brand-name .secondary {
    display: block;
    font-size: 58px;
    letter-spacing: 3px;
    margin-top: 10px;
  }
  .contact {
    position: absolute;
    right: 60px;
    top: 322px;
    text-align: right;
    color: var(--text-grey);
  }
  .contact .person {
    margin: 0 0 22px;
    font-size: 48px;
    font-weight: 700;
    color: var(--brand-blue);
    line-height: 1;
  }
  .contact .details {
    margin: 0;
    padding: 0;
    list-style: none;
    font-size: 36px;
    line-height: 48px;
  }
</style>
</head>
<body>
  <main class="card">
    <svg class="accent-bands" viewBox="0 0 1200 686" aria-hidden="true">
      <polygon points="436,0 1200,0 1200,69 509,69"/>
      <polygon points="0,615 700,615 769,686 0,686"/>
    </svg>

    <div class="brand">
      <div class="brand-square" aria-hidden="true"></div>
      <div class="brand-name">
        <span class="primary">Tarvo</span>
        <span class="secondary">Commercial</span>
      </div>
    </div>

    <section class="contact">
      <h1 class="person">Colin Farrow</h1>
      <ul class="details">
        <li>Lic# 07281549</li>
        <li>415.555.0172</li>
        <li>colin@tarvo-commercial.example</li>
        <li>www.tarvo-commercial.example</li>
      </ul>
    </section>
  </main>
</body>
</html>
```